new letterhead/envelope/business card design for law firm

please see attached pdf of current letterhead, envelope and business card. I am also attaching my new logo that I would like to be used. basically, I am looking to refresh and simplify my letterhead/stationary and business card, keeping the following in mind:

overall, I am going for the following look:

-simple,
-modern,
-classy,
-professional

Target Market(s)

law firm clients

Industry/Entity Type

Law Firm

Contact Information for Business Card

see attachment

Font styles to use
Sans Serif

Requirements
Must have
• overall, I am going for the following look:
• -simple,
• -modern,
• -classy,
• -professional
Nice to have
• same as above
Should not have
• no serif fonts

```html
<!DOCTYPE html>
<html lang="en">
<head>
<meta charset="utf-8">
<title>Hollis Law — Stationery</title>
<link href="https://fonts.googleapis.com/css2?family=Montserrat:wght@500&family=Poppins:wght@300&family=Roboto:wght@400&family=Roboto+Condensed:wght@700&display=swap" rel="stylesheet">
<style>
:root{
  --bg:#dcdcdc;
  --paper:#f6f6f6;
  --navy:#0b2a4e;
  --green:#1f5a33;
  --ink:#3a3a3a;
  --muted:#555;
  --shadow:0 2px 6px rgba(0,0,0,.18);
}
*{margin:0;padding:0;box-sizing:border-box}
html,body{width:1200px;height:877px;overflow:hidden;background:var(--bg)}
.canvas{position:relative;width:1200px;height:877px;font-family:"Roboto",sans-serif;color:var(--ink)}
.sheet{position:absolute;background:var(--paper);box-shadow:var(--shadow)}
.abs{position:absolute}
.seal{position:absolute;border-radius:50%;background:var(--navy)}
.brand{position:absolute;font-family:"Montserrat",sans-serif;font-weight:500;color:var(--navy);letter-spacing:2px;white-space:nowrap}
.rule{position:absolute;height:1px;background:var(--green)}
.person{font-family:"Roboto Condensed",sans-serif;font-weight:700;color:var(--navy)}
.cred{color:var(--green)}

/* letterhead */
.letterhead{left:58px;top:64px;width:527px;height:742px}
.letterhead .head{right:43px;top:85px;text-align:right;font-size:8px;line-height:9.5px;color:var(--muted)}
.letterhead .head .person{font-size:9px;margin-bottom:2px}
.salutation{left:46px;top:207px;font-family:"Poppins",sans-serif;font-weight:300;font-size:13px;color:#444}
.body{left:46px;top:247px;width:438px;font-family:"Poppins",sans-serif;font-weight:300;font-size:7.1px;line-height:11.4px;color:#444;text-align:justify}
.body p{margin-bottom:11.4px}
.closing{left:46px;top:485px;font-family:"Poppins",sans-serif;font-weight:300;font-size:7.5px;color:#444}
.signature{left:42px;top:518px;width:96px;height:42px;background:linear-gradient(90deg,#3f63ad33,#3f63ad11);border-radius:4px}
.contact{font-size:7.8px;line-height:10.4px;color:#444}
.contact li{list-style:none;display:flex;align-items:center;gap:4px}
.contact svg{width:7px;height:7px;fill:var(--navy)}
.letterhead .contact{left:47px;top:685px}
.letterhead .address{right:45px;top:695px;text-align:right;font-size:7.8px;line-height:10.4px;color:#444}

/* business card */
.card-front{left:606px;top:88px;width:252px;height:144px}
.card-front .head{right:16px;top:28px;text-align:right;font-size:6px;line-height:8px}
.card-front .head .person{font-size:8.5px;line-height:11px}
.card-front .contact{left:16px;top:107px;font-size:6px;line-height:8px}
.card-front .contact svg{width:5px;height:5px}
.card-front .address{right:16px;top:108px;text-align:right;font-size:6px;line-height:8px;color:#444}
.card-back{left:878px;top:88px;width:252px;height:144px;background:var(--navy)}
.card-back .ring{left:86px;top:27px;width:80px;height:80px;border:2px solid #fff;border-radius:50%;display:flex;align-items:center;justify-content:center}
.card-back .ring span{font-family:"Montserrat",sans-serif;font-weight:500;color:#fff;font-size:8.5px;letter-spacing:1px;white-space:nowrap;text-align:center}
.card-back .url{left:0;right:0;top:124px;text-align:center;color:#fff;font-size:6px;letter-spacing:3px}

/* envelopes */
.envelope-back{left:603px;top:269px;width:531px;height:240px}
.envelope-back .flap{left:0;top:0;width:531px;height:76px}
.envelope-front{left:603px;top:562px;width:533px;height:242px}
.envelope-front .address{left:0;width:200px;top:97px;text-align:center;font-size:7.5px;line-height:9px;color:#333}
</style>
</head>
<body>
<div class="canvas">

  <!-- Letterhead -->
  <section class="sheet letterhead">
    <div class="seal" style="left:84px;top:48px;width:44px;height:44px"></div>
    <div class="brand" style="left:46px;top:96px;font-size:20px">HOLLIS LAW</div>
    <div class="rule" style="left:46px;top:124px;width:438px"></div>
    <div class="abs head">
      <div class="person">DANIEL R. HOLLIS, ESQ.</div>
      <div>Licensed in NC and FL</div>
      <div>Board Certified in Civil Trial Law, by NTAB</div>
    </div>

    <div class="abs salutation">Dear Mr. Carter,</div>
    <div class="abs body">
      <p>Lorem ipsum dolor sit amet, consectetur adipiscing elit. Donec orci purus, luctus vitae dignissim eu, iaculis sed purus. Vivamus faucibus, ipsum nec aliquet viverra, leo mauris condimentum ligula, sit amet sagittis enim ligula quis arcu. Nam egestas tortor id nisi porttitor mattis. In tortor ante, ultricies in suscipit a, tempus non massa. Vivamus et auctor mi. Fusce vel massa nulla. Phasellus nec eros mauris, et scelerisque orci.</p>
      <p>Donec malesuada orci vitae nulla accumsan porta a id massa. Quisque accumsan iaculis magna sit amet fringilla. Maecenas consequat, magna eget tincidunt semper, odio nibh rutrum mi, id feugiat ante nisi eu risus. Vestibulum nunc orci, rhoncus a placerat in, ultricies in mi. Cras mattis varius eros, vel fringilla nisi suscipit eget. Quisque scelerisque sagittis nulla at porttitor.</p>
      <p>Sed id augue vitae urna euismod commodo aliquet a quam. Pellentesque arcu velit, cursus et malesuada ut, consequat et diam. Nullam erat sem, rhoncus id ullamcorper vitae, rhoncus et arcu. In ultricies ultricies nulla, ut rutrum nisi iaculis at. Donec eu magna a metus ornare faucibus. Fusce aliquet faucibus ultricies. Morbi semper, est id tincidunt gravida, sem arcu adipiscing lacus, ac bibendum nulla leo eu purus. Quisque nec diam sed risus consectetur a ccumsan quis quis nibh. Vestibulum id purus lorem.</p>
      <p>It is a long established fact that a reader will be distracted by the readable content of a page when looking at its layout. The point of using Lorem Ipsum is that it has a more-or-less normal distribution of letters, as opposed to using 'Content here, content here', making it look like readable English. Many desktop publishing packages</p>
    </div>
    <div class="abs closing">Sincerely,</div>
    <div class="abs signature" role="img" aria-label="Handwritten signature of Paul Carter"></div>

    <ul class="abs contact">
      <li><svg viewBox="0 0 10 10"><path d="M2 0h2l1 3-1.5 1a6 6 0 0 0 2.5 2.5L7 5l3 1v2c0 1-1 2-2 2A8 8 0 0 1 0 2c0-1 1-2 2-2z"/></svg>555.014.2231</li>
      <li><svg viewBox="0 0 10 10"><path d="M2 0h6v3H2zM0 3.5h10V8H8v2H2V8H0zM3 7v2h4V7z"/></svg>555.014.9186</li>
      <li><svg viewBox="0 0 10 10"><circle cx="5" cy="5" r="5"/></svg>www.hollislawpa.com</li>
    </ul>
    <div class="abs address">2240 Linden Court<br>Suite 410, Raleigh, NC 27610</div>
  </section>

  <!-- Business card front -->
  <section class="sheet card-front">
    <div class="seal" style="left:51px;top:13px;width:28px;height:28px"></div>
    <div class="brand" style="left:16px;top:44px;font-size:13px;letter-spacing:1.5px">HOLLIS LAW</div>
    <div class="rule" style="left:16px;top:60px;width:220px"></div>
    <div class="abs head">
      <div class="person">DANIEL R. HOLLIS, ESQ</div>
      <div class="cred">Licensed in NC and FL. Board</div>
      <div class="cred">Certified in Civil Trial Law by NTAB</div>
    </div>
    <ul class="abs contact">
      <li><svg viewBox="0 0 10 10"><path d="M2 0h2l1 3-1.5 1a6 6 0 0 0 2.5 2.5L7 5l3 1v2c0 1-1 2-2 2A8 8 0 0 1 0 2c0-1 1-2 2-2z"/></svg>555.014.2231</li>
      <li><svg viewBox="0 0 10 10"><path d="M2 0h6v10H2zM3 1v7h4V1z"/></svg>555.014.7702</li>
      <li><svg viewBox="0 0 10 10"><path d="M2 0h6v3H2zM0 3.5h10V8H8v2H2V8H0zM3 7v2h4V7z"/></svg>555.014.9186</li>
    </ul>
    <div class="abs address">2240 Linden Court<br>Suite 410, Raleigh, NC 27610<br>www.hollislawpa.com</div>
  </section>

  <!-- Business card back -->
  <section class="sheet card-back">
    <div class="abs ring"><span>HOLLIS LAW</span></div>
    <div class="abs url">www.hollislawpa.com</div>
  </section>

  <!-- Envelope back -->
  <section class="sheet envelope-back">
    <svg class="abs flap" viewBox="0 0 531 76" aria-hidden="true">
      <path d="M0 0H531L522 12C512 50 505 70 485 74H46C26 70 19 50 9 12Z" fill="#f2f2f2" stroke="#d6d6d6"/>
    </svg>
    <div class="seal" style="left:250px;top:20px;width:35px;height:35px"></div>
  </section>

  <!-- Envelope front -->
  <section class="sheet envelope-front">
    <div class="seal" style="left:79px;top:25px;width:38px;height:38px"></div>
    <div class="brand" style="left:29px;top:68px;font-size:17px">HOLLIS LAW</div>
    <div class="rule" style="left:29px;top:90px;width:142px"></div>
    <div class="abs address">2240 Linden Court,<br>Suite 410, Raleigh, NC 27610</div>
  </section>

</div>
</body>
</html>
```